Conceptual Model Diagram for Replacing Medication with Behavior to Support Weight Loss Maintenance

Design a figure of a conceptual model that needs to be inserted into a word document for a PSF grant. This conceptual model illustrates how behavioral strategies can replace the regulatory functions lost after AOM discontinuation. The intervention targets three core vulnerabilities—appetite resurgence, metabolic inflexibility, and suboptimal mindstate—through the domains of Food, Physical Activity, and Mind. Sustained weight loss maintenance occurs at the intersection of these domains. The intervention is delivered within a design framework that makes behaviors easier to perform, aligns them with identity, and reinforces them through virtual support and community, ensuring real-world feasibility and long-term adherence.
Target Market(s)
PSF reviewers
Industry/Entity Type
academic
Other font styles liked:
- arial
Requirements
Must have
- see my attached description

```html
<!DOCTYPE html>
<html lang="en">
<head>
<meta charset="utf-8">
<title>Conceptual Model for Replacing Medication with Behavior to Support Weight Loss Maintenance</title>
<link href="https://fonts.googleapis.com/css2?family=Archivo+Black&family=Arimo:wght@400;700&display=swap" rel="stylesheet">
<style>
  :root {
    --canvas: #f2f5f5;
    --ink: #235447;
    --muted: #7f8c8b;
    --frame: #879a98;
    --core: #dce3e2;
    --appetite: #c77dff;
    --appetite-label: #c462f0;
    --appetite-fill: #e9dff6;
    --appetite-deep: #e3cdf9;
    --mind: #e58a96;
    --mind-label: #d45d6c;
    --mind-fill: #f0e0e4;
    --mind-deep: #efcdd5;
    --metabolic: #6ff0c0;
    --metabolic-label: #5ee8b5;
    --metabolic-fill: #d8f5ea;
    --metabolic-deep: #c0f4e0;
    --black: #111;
  }
  * { box-sizing: border-box; margin: 0; padding: 0; }
  html, body { width: 1200px; height: 1200px; overflow: hidden; background: var(--canvas); }
  .canvas { position: relative; width: 1200px; height: 1200px; font-family: "Arimo", Arial, sans-serif; }
  .model-title {
    position: absolute; top: 270px; left: 0; width: 1200px; text-align: center;
    font-family: "Archivo Black", "Arial Black", sans-serif; font-size: 20px;
    letter-spacing: 0.6px; color: var(--ink);
  }
  .model-diagram { position: absolute; inset: 0; width: 1200px; height: 1200px; }
  .legend {
    position: absolute; left: 778px; top: 362px; width: 374px; height: 209px;
    background: var(--core); border: 3px solid var(--frame); border-radius: 12px;
    padding: 12px 0 0 13px;
  }
  .legend-item { height: 69px; }
  .legend-term { font-weight: 700; font-size: 17px; color: var(--ink); line-height: 1; margin-bottom: 10px; }
  .legend-desc { font-weight: 700; font-size: 13.6px; color: var(--muted); line-height: 1; }
  svg text { font-family: "Arimo", Arial, sans-serif; font-weight: 700; }
</style>
</head>
<body>
<div class="canvas">
  <h1 class="model-title">Conceptual Model for Replacing Medication with Behavior to Support Weight Loss Maintenance</h1>

  <svg class="model-diagram" viewBox="0 0 1932 1932" aria-label="Venn diagram of Food, Physical Activity and Mind domains">
    <defs>
      <clipPath id="clip-top"><circle cx="766" cy="950" r="273"/></clipPath>
      <clipPath id="clip-left"><circle cx="604" cy="1178" r="273"/></clipPath>
      <clipPath id="clip-right"><circle cx="929" cy="1178" r="273"/></clipPath>
      <mask id="mask-food">
        <circle cx="766" cy="950" r="223" fill="#fff"/>
        <circle cx="604" cy="1178" r="300" fill="#000"/>
        <circle cx="929" cy="1178" r="300" fill="#000"/>
      </mask>
      <mask id="mask-mind">
        <circle cx="604" cy="1178" r="223" fill="#fff"/>
        <circle cx="766" cy="950" r="300" fill="#000"/>
        <circle cx="929" cy="1178" r="300" fill="#000"/>
      </mask>
      <mask id="mask-activity">
        <circle cx="929" cy="1178" r="223" fill="#fff"/>
        <circle cx="766" cy="950" r="300" fill="#000"/>
        <circle cx="604" cy="1178" r="300" fill="#000"/>
      </mask>
      <path id="arc-easy" d="M 474 950 A 292 292 0 0 1 1058 950"/>
      <path id="arc-support" d="M 294 1178 A 310 310 0 0 0 914 1178"/>
      <path id="arc-identity" d="M 619 1178 A 310 310 0 0 0 1239 1178"/>
    </defs>

    <!-- domain circles -->
    <g class="domain-fills">
      <circle cx="766" cy="950" r="273" fill="var(--appetite-fill)"/>
      <circle cx="604" cy="1178" r="273" fill="var(--mind-fill)"/>
      <circle cx="929" cy="1178" r="273" fill="var(--metabolic-fill)"/>
    </g>
    <g class="domain-cores">
      <rect width="1932" height="1932" fill="var(--appetite-deep)" mask="url(#mask-food)"/>
      <rect width="1932" height="1932" fill="var(--mind-deep)" mask="url(#mask-mind)"/>
      <rect width="1932" height="1932" fill="var(--metabolic-deep)" mask="url(#mask-activity)"/>
    </g>
    <g class="domain-overlaps">
      <g clip-path="url(#clip-top)"><circle cx="604" cy="1178" r="273" fill="var(--mind-fill)"/></g>
      <g clip-path="url(#clip-top)"><circle cx="929" cy="1178" r="273" fill="var(--appetite-fill)"/></g>
      <g clip-path="url(#clip-left)"><circle cx="929" cy="1178" r="273" fill="var(--metabolic-fill)"/></g>
    </g>
    <g class="domain-separators" fill="none" stroke="var(--canvas)" stroke-width="18">
      <circle cx="766" cy="950" r="273"/>
      <circle cx="604" cy="1178" r="273"/>
      <circle cx="929" cy="1178" r="273"/>
    </g>
    <g class="domain-outlines" fill="none" stroke-width="6">
      <circle cx="766" cy="950" r="273" stroke="var(--appetite)"/>
      <circle cx="604" cy="1178" r="273" stroke="var(--mind)"/>
      <circle cx="929" cy="1178" r="273" stroke="var(--metabolic)"/>
    </g>

    <!-- shared outcome -->
    <g class="outcome" clip-path="url(#clip-top)">
      <g clip-path="url(#clip-left)">
        <circle cx="929" cy="1178" r="273" fill="var(--core)" stroke="var(--frame)" stroke-width="12"/>
        <circle cx="604" cy="1178" r="273" fill="none" stroke="var(--frame)" stroke-width="12"/>
        <circle cx="766" cy="950" r="273" fill="none" stroke="var(--frame)" stroke-width="12"/>
      </g>
    </g>
    <g class="outcome-label" fill="var(--ink)" font-size="29" text-anchor="middle">
      <text x="766" y="1071">Sustained</text>
      <text x="766" y="1104">Weight</text>
      <text x="766" y="1137">Loss</text>
      <text x="766" y="1171">Maintenance</text>
    </g>

    <!-- domain labels -->
    <g class="domain-labels" fill="var(--ink)" font-size="29" text-anchor="middle">
      <text x="766" y="810">Food</text>
      <text x="497" y="1266">Mind</text>
      <text x="1046" y="1250">Physical</text>
      <text x="1052" y="1283">Activity</text>
    </g>

    <!-- domain icons -->
    <g class="domain-icons" stroke-width="3">
      <circle cx="595" cy="1015" r="38" fill="none" stroke="var(--mind)"/>
      <circle cx="595" cy="1015" r="22" fill="var(--mind)" opacity="0.85" role="img" aria-label="Brain icon"/>
      <circle cx="939" cy="1015" r="38" fill="none" stroke="var(--appetite)"/>
      <g fill="var(--appetite-label)" stroke="none" role="img" aria-label="Fork and spoon icon">
        <rect x="925" y="995" width="3" height="16" rx="1.5"/>
        <rect x="930" y="995" width="3" height="16" rx="1.5"/>
        <rect x="935" y="995" width="3" height="16" rx="1.5"/>
        <rect x="925" y="1008" width="13" height="6" rx="3"/>
        <rect x="929" y="1010" width="5" height="28" rx="2.5"/>
        <ellipse cx="948" cy="1003" rx="6" ry="10"/>
        <rect x="945.5" y="1008" width="5" height="30" rx="2.5"/>
      </g>
      <circle cx="766" cy="1305" r="38" fill="none" stroke="var(--metabolic)"/>
      <circle cx="766" cy="1305" r="22" fill="var(--metabolic)" opacity="0.8" role="img" aria-label="Runner icon"/>
    </g>

    <!-- vulnerabilities -->
    <g class="vulnerability appetite">
      <line x1="766" y1="605" x2="766" y2="666" stroke="var(--appetite)" stroke-width="3"/>
      <circle cx="766" cy="677" r="11" fill="var(--canvas)" stroke="var(--appetite)" stroke-width="3"/>
      <text x="766" y="543" fill="var(--appetite-label)" font-size="33" text-anchor="middle">Appetite</text>
      <text x="766" y="582" fill="var(--appetite-label)" font-size="33" text-anchor="middle">Resurgence</text>
    </g>
    <g class="vulnerability mindstate">
      <line x1="270" y1="1257" x2="331" y2="1257" stroke="var(--mind)" stroke-width="3"/>
      <circle cx="342" cy="1257" r="11" fill="var(--canvas)" stroke="var(--mind)" stroke-width="3"/>
      <text x="255" y="1246" fill="var(--mind-label)" font-size="33" text-anchor="end">Suboptimal</text>
      <text x="255" y="1285" fill="var(--mind-label)" font-size="33" text-anchor="end">Mindstate</text>
    </g>
    <g class="vulnerability metabolic">
      <line x1="1202" y1="1257" x2="1263" y2="1257" stroke="var(--metabolic)" stroke-width="3"/>
      <circle cx="1191" cy="1257" r="11" fill="var(--canvas)" stroke="var(--metabolic)" stroke-width="3"/>
      <text x="1277" y="1246" fill="var(--metabolic-label)" font-size="33">Metabolic</text>
      <text x="1277" y="1285" fill="var(--metabolic-label)" font-size="33">Inflexibility</text>
    </g>

    <!-- design framework -->
    <g class="framework-labels" fill="var(--black)" font-size="25">
      <text><textPath href="#arc-easy" startOffset="21%">Make it Easy</textPath></text>
      <text><textPath href="#arc-support" startOffset="15%">Virtual Support and Social Connection</textPath></text>
      <text><textPath href="#arc-identity" startOffset="52%">Align with identity</textPath></text>
    </g>
  </svg>

  <aside class="legend">
    <div class="legend-item">
      <p class="legend-term">Make it Easy</p>
      <p class="legend-desc">Habits, routines, environment, low friction</p>
    </div>
    <div class="legend-item">
      <p class="legend-term">Align with identity</p>
      <p class="legend-desc">Self concept, maintain IT model, internalization</p>
    </div>
    <div class="legend-item">
      <p class="legend-term">Virtual Support and Social Connection</p>
      <p class="legend-desc">Accessibility, community, shared accountability</p>
    </div>
  </aside>
</div>
</body>
</html>
```